Heron Ridge Distillery Bottle Label Design

We need a label design for a product called "Cedar Hollow Straight Bourbon Whiskey". The bottle has two embossments on the side and an image printed on the back that will show through when looking from the front (shown in the attached image). It's made of 30% rye and 70% corn; images of the ingredients can be incorporated into the label design. We are a distillery that produces whiskey and bourbon from local farmers around the area. We focus on the quality of the ingredients and using the recipes passed down from generation to generation. We like a straight forward design using two colors maximum. The background will be brown once filled with the bourbon, so it must contrast against it (i.e. white and other lighter colors). The Heron Ridge Distillery logo must be present on the bottle front, as well as 750 ml, 84 PROOF, 42% ALC/VOL.

Target Market(s)

Craft whiskey consumers.

Industry/Entity Type

Product

Colors
fee18a
fbe7d2
fff3d1
fefcee
fefdec
fdf9cf

Requirements
Must have
• 750 ml, 84 PROOF, 42% ALC/VOL. Aged for 3 years.The Heron Ridge Distillery logo must be present on the bottle. Only two colors on label.
Nice to have
• Story of how we are a micro distillery making hand crafted whiskey.
Should not have
• False or misleading print.

```html
<!DOCTYPE html>
<html lang="en">
<head>
<meta charset="utf-8">
<title>Cedar Hollow Straight Bourbon Whiskey — Heron Ridge Distillery Label</title>
<link rel="stylesheet" href="https://fonts.googleapis.com/css2?family=Alfa+Slab+One&family=Arvo&family=Tinos&family=Archivo+Black&display=swap">
<style>
  :root {
    --bg-top: #0b0909;
    --bg-bottom: #2e1113;
    --label-white: #ffffff;
    --accent-yellow: #fff200;
    --ink-dark: #111111;
  }
  * { margin: 0; padding: 0; box-sizing: border-box; }
  html, body { width: 1200px; height: 999px; overflow: hidden; }
  body { background: var(--bg-top); }
  .label {
    position: relative;
    width: 1200px;
    height: 999px;
    overflow: hidden;
    background: linear-gradient(170deg, var(--bg-top) 0%, #231516 45%, var(--bg-bottom) 100%);
    color: var(--label-white);
  }
  .brand-mark {
    position: absolute;
    left: 160px;
    top: 18px;
    width: 284px;
    height: 284px;
  }
  .brand-mark svg { position: absolute; inset: 0; }
  .brand-name {
    position: absolute;
    left: 60px;
    top: 118px;
    width: 164px;
    text-align: center;
    font-family: "Archivo Black", sans-serif;
    font-size: 24px;
    line-height: 26px;
    color: var(--ink-dark);
  }
  .product {
    position: absolute;
    left: 40px;
    width: 524px;
    text-align: center;
  }
  .product-name {
    top: 364px;
    font-family: "Arvo", serif;
    font-size: 38px;
    letter-spacing: 3px;
  }
  .product-type {
    top: 432px;
    font-family: "Alfa Slab One", serif;
    font-size: 64px;
    line-height: 76px;
    letter-spacing: 1px;
  }
  .product-age {
    top: 670px;
    font-family: "Arvo", serif;
    font-size: 30px;
    letter-spacing: 3px;
  }
  .volume-icon {
    position: absolute;
    left: 268px;
    top: 826px;
  }
  .volume {
    position: absolute;
    left: 200px;
    width: 204px;
    top: 938px;
    text-align: center;
    font-family: "Tinos", serif;
    font-size: 32px;
  }
  .story {
    position: absolute;
    left: 630px;
    width: 550px;
    top: 150px;
    text-align: center;
    font-family: "Tinos", serif;
    font-size: 33px;
    line-height: 44.6px;
  }
  .story .initial { font-size: 52px; line-height: 40px; }
  .mash-bill {
    position: absolute;
    left: 600px;
    top: 782px;
    width: 600px;
    height: 52px;
    display: flex;
    font-family: "Tinos", serif;
    font-size: 32px;
    color: var(--ink-dark);
  }
  .mash-rye { width: 179px; background: var(--label-white); display: flex; align-items: center; justify-content: center; }
  .mash-corn { flex: 1; background: var(--accent-yellow); display: flex; align-items: center; justify-content: center; }
  .strength {
    position: absolute;
    left: 700px;
    width: 410px;
    top: 864px;
    text-align: center;
    font-family: "Tinos", serif;
    font-size: 33px;
    line-height: 37px;
  }
</style>
</head>
<body>
<main class="label">
  <div class="brand-mark">
    <svg width="284" height="284" viewBox="0 0 284 284" aria-hidden="true">
      <polygon points="142,0 284,142 142,284 0,142" fill="var(--label-white)"/>
    </svg>
    <div class="brand-name">Heron Ridge Distillery</div>
  </div>

  <div class="product product-name">Cedar Hollow</div>
  <h1 class="product product-type">STRAIGHT<br>BOURBON<br>WHISKEY.</h1>
  <div class="product product-age">Aged 3 Years</div>

  <svg class="volume-icon" width="68" height="94" viewBox="0 0 68 94" aria-hidden="true">
    <path d="M34 0 C40 22 68 46 68 60 A34 34 0 0 1 0 60 C0 46 28 22 34 0 Z" fill="var(--label-white)"/>
  </svg>
  <div class="volume">750 ml.</div>

  <p class="story"><span class="initial">T</span>here’s nothing complicated<br>about Cedar Hollow Straight<br>Bourbon. Local farmers supply<br>home-grown ingredients, and<br>we supply our family recipe.<br>After a few years of maturation,<br>our bourbon is distilled and<br>shipped out to the masses.<br>Quality and consistency are<br>our trademark, using tried and<br>true methods passed down from<br>generation to generation… and<br>into your glass. Enjoy.</p>

  <div class="mash-bill">
    <div class="mash-rye">30% Rye</div>
    <div class="mash-corn">70% corn</div>
  </div>

  <div class="strength">42% alcohol<br>84 Proof</div>
</main>
</body>
</html>
```